Cyber Security Site Design (Products & Consulting)

I need my website redesigned to be engaging, clean, efficient and modern. My company (when its up and running) is going to be concentrated on two things: a few specific products for cyber security as well as cyber security consulting services. The background I bring to the field is having worked with small companies all the way to the largest government organizations and advising them on their security posture and how to improve it. We need the ability to add products and services easily.

For a sample product, you can use either Heron (http://www.heron-relay.example/) or Vorlant Greystone (https://www.vorlant.example/products/relay-hub-and-layered-access-portal).

It will replace https://talmerocharts.example/

Target Market(s)

Cyber Security professionals in all verticals

Coding

Coded - Design and coding required

Number of Pages Required

4 page

Font styles to use
Sans Serif

Colors
6b449b

Requirements
Must have
• Ability to easily modify
• Have main page
• Have product specific pages
• Have consulting services pages
• Have executive team information
• Clean, modern design
• Usage of the logo and its color scheme
Nice to have
• I like the idea of a left collapsed sidebar (so icons only) that can expand for text.
• I am also open to a very unique landing page, possibly a shape in the middle (hexagons maybe?) with each of the options there.
Should not have
• Nothing that looks like it came out of a hacker movie

```html
<!DOCTYPE html>
<html lang="en">
<head>
<meta charset="utf-8">
<title>Talmero Charts — Cyber Security</title>
<link href="https://fonts.googleapis.com/css2?family=Roboto:wght@300;400;500;700;900&display=swap" rel="stylesheet">
<style>
:root{
  --purple:#6b449b;
  --purple-dark:#58357f;
  --purple-soft:#7d56ad;
  --ink:#2b2b2b;
  --muted:#555;
  --charcoal:#4a4a4c;
  --footer:#2e2d31;
  --light:#f2f2f2;
  --grey:#dcdcdc;
  --orange:#f26b1d;
  --white:#fff;
}
*{margin:0;padding:0;box-sizing:border-box}
html,body{width:1200px;height:3175px;overflow:hidden}
body{position:relative;font-family:"Roboto",Arial,sans-serif;color:var(--ink);background:var(--white)}
.abs{position:absolute}
svg{display:block}

/* top bar */
.topbar{left:0;top:0;width:1200px;height:30px;background:var(--purple);color:#fff;font-size:12px}
.topbar .contact{left:160px;top:7px;display:flex;gap:18px;align-items:center}
.topbar .contact span{display:flex;gap:5px;align-items:center}
.topbar .search{left:768px;top:5px;width:140px;height:20px;border:1px solid #c9b6e0;border-radius:2px;padding:2px 6px;font-size:10px;display:flex;justify-content:space-between;align-items:center}
.topbar .cart{left:922px;top:7px;font-size:11px;display:flex;gap:6px;align-items:center}

/* header */
.header{left:0;top:30px;width:1200px;height:76px;background:#fff}
.brand{left:160px;top:14px;display:flex;align-items:center;gap:10px}
.brand .mark{width:44px;height:44px;background:var(--purple)}
.brand .name{font-size:34px;font-weight:700;color:var(--purple);letter-spacing:.5px}
.nav{left:660px;top:33px;display:flex;gap:24px;font-size:12px;font-weight:500;color:#222}

/* hero */
.hero-photo{left:0;top:106px;width:1200px;height:529px;background:linear-gradient(180deg,#c9d2da 0%,#9aa6b2 45%,#3d434c 100%)}
.welcome-band{left:0;top:635px;width:1200px;height:520px;background:linear-gradient(180deg,#6b449b,#5f3c8b)}
.welcome-card{left:163px;top:554px;width:876px;height:553px;background:var(--light);border-top:3px solid var(--purple);box-shadow:0 4px 14px rgba(0,0,0,.2)}
.welcome-kicker{left:0;top:52px;width:876px;text-align:center;font-size:22px;font-weight:300;color:#333;letter-spacing:.5px}
.welcome-title{left:0;top:74px;width:876px;text-align:center;font-size:40px;font-weight:700;color:var(--purple)}
.welcome-text{left:68px;top:128px;width:740px;text-align:center;font-size:11.5px;line-height:1.6;color:var(--muted)}
.feature{width:254px;height:152px;background:#fff;border:1px solid #ccc;text-align:center;padding-top:14px}
.feature .icon{margin:0 auto 8px;width:50px;height:50px}
.feature h3{font-size:15px;font-weight:400;color:#222;margin-bottom:4px}
.feature p{font-size:11px;line-height:1.35;color:#444;padding:0 24px}
.hexagon{left:500px;top:790px}

/* about */
.about-photo{left:161px;top:1206px;width:406px;height:466px;border:3px solid #c9c9c9;background:linear-gradient(180deg,#eef0f2,#c8c3bf 55%,#3d3c42)}
.about-box{left:521px;top:1255px;width:518px;height:337px;background:var(--charcoal);color:#ddd;padding:24px 28px}
.about-box h2{font-size:28px;font-weight:700;color:#fff;padding-bottom:8px;border-bottom:1px solid #888;margin-bottom:14px;width:460px}
.about-box p{font-size:9.8px;line-height:1.5;margin-bottom:10px;text-align:justify}
.about-social{left:28px;top:272px;display:flex;gap:10px}
.ring{width:28px;height:28px;border-radius:50%;border:2px solid #fff;background:transparent}
.read-more{right:36px;top:278px;font-size:14px;color:#fff}
.pager{display:flex;gap:6px}
.pager span{width:32px;height:32px;background:var(--purple);display:flex;align-items:center;justify-content:center}

/* products */
.products{left:0;top:1729px;width:1200px;height:489px;background:linear-gradient(180deg,#e3e3e3,#d3d3d3)}
.section-title{left:0;top:44px;width:1200px;text-align:center;font-size:46px;font-weight:300;color:#222}
.section-title b{font-weight:900}
.ribbon{left:477px;top:95px;width:246px;height:23px;background:var(--purple);color:#fff;font-size:13px;font-weight:500;letter-spacing:1px;text-align:center;line-height:23px}
.product{width:277px;height:296px}
.product .shot{width:277px;height:186px}
.product .panel{position:absolute;left:15px;top:161px;width:245px;height:135px;background:var(--purple);color:#fff;text-align:center;padding-top:14px}
.product h3{font-size:14px;font-weight:700;margin-bottom:6px}
.product p{font-size:10.5px;line-height:1.35;padding:0 16px;margin-bottom:10px}
.shop{display:inline-block;background:var(--orange);color:#fff;font-size:12px;font-weight:700;padding:6px 18px}
.round-arrow{width:34px;height:34px;border-radius:50%;background:#8d8d8d;display:flex;align-items:center;justify-content:center}

/* team */
.team-banner{left:396px;top:2258px;width:400px;height:49px}
.team-banner .label{left:0;top:0;width:400px;text-align:center;line-height:49px;color:#fff;font-size:34px;font-weight:500}
.member{background:linear-gradient(180deg,#e4e8ec,#b9bec5 60%,#3f434b)}
.member.lead{background:linear-gradient(180deg,#dfe2e6,#c5c8cc 60%,#2f3440);box-shadow:0 0 10px rgba(0,0,0,.25)}
.name-tag{left:501px;top:2537px;width:178px;height:45px;background:var(--purple);color:#fff;text-align:center;padding-top:5px}
.name-tag strong{display:block;font-size:16px;font-weight:500}
.name-tag small{font-size:11px}
.outline-arrow{width:30px;height:30px;border-radius:50%;border:2px solid var(--purple);display:flex;align-items:center;justify-content:center}
.team-text{left:240px;top:2604px;width:720px;text-align:center;font-size:11px;line-height:1.6;color:#555}
.team-social{left:533px;top:2657px;display:flex;gap:8px}
.team-social span{width:26px;height:26px;border:1px solid var(--orange)}

/* payments */
.payments{left:0;top:2723px;width:1200px;height:74px;background:#f0f0f0}
.pay{top:19px;width:62px;height:36px;background:#fff;border:1px solid #ccc;font-size:11px;font-weight:700;color:#333;display:flex;align-items:center;justify-content:center}

/* footer */
.footer{left:0;top:2797px;width:1200px;height:341px;background:var(--footer);color:#ccc}
.info-box{top:34px;width:270px;height:68px;border:1px solid #6a6a70;display:flex;align-items:center;gap:14px;padding-left:0;font-size:11px;line-height:1.5}
.info-box .ico{width:38px;height:38px;background:var(--purple);display:flex;align-items:center;justify-content:center;flex-shrink:0}
.foot-col{top:140px}
.foot-col h4{font-size:17px;font-weight:500;color:#fff;margin-bottom:18px;letter-spacing:.5px}
.foot-col p{font-size:11px;line-height:1.5;width:270px}
.foot-col .more{font-size:10px;margin-top:8px}
.foot-social{display:flex;gap:10px;margin-top:18px}
.foot-social span{width:26px;height:26px;border-radius:50%;background:#6a6a70}
.foot-list{list-style:none;font-size:12px;line-height:27px}
.foot-list li::before{content:"» ";}
.email-field{width:204px;height:40px;background:#d9d9d9;font-size:11px;color:#777;padding:13px 10px}
.subscribe{margin-top:12px;width:96px;height:30px;background:var(--purple);color:#fff;font-size:12px;font-weight:700;text-align:center;line-height:30px}
.copyright{left:0;top:3138px;width:1200px;height:37px;background:var(--purple);color:#fff;font-size:11px;text-align:center;line-height:37px}
</style>
</head>
<body>

<!-- top bar -->
<div class="abs topbar">
  <div class="abs contact">
    <span><svg width="13" height="10" viewBox="0 0 13 10"><rect x=".5" y=".5" width="12" height="9" fill="#fff"/><path d="M.5 .5 6.5 5.5 12.5 .5" stroke="#6b449b" fill="none"/></svg>info@talmerocharts.example</span>
    <span><svg width="7" height="12" viewBox="0 0 7 12"><rect x=".5" y=".5" width="6" height="11" rx="1" fill="none" stroke="#fff"/></svg>000.000.0000</span>
  </div>
  <div class="abs search">Search here... <svg width="10" height="10" viewBox="0 0 10 10"><circle cx="4" cy="4" r="3" stroke="#fff" fill="none" stroke-width="1.4"/><path d="M6.3 6.3 9.5 9.5" stroke="#fff" stroke-width="1.4"/></svg></div>
  <div class="abs cart"><svg width="16" height="16" viewBox="0 0 16 16"><circle cx="8" cy="8" r="8" fill="#fff"/><path d="M4 5h1.5l1.2 5h4.5l1-3.5H6" stroke="#6b449b" fill="none" stroke-width="1.2"/></svg>Cart: 0 items - $0.00</div>
</div>

<!-- header -->
<header class="abs header">
  <div class="abs brand"><span class="mark"></span><span class="name">TALMERO CHARTS</span></div>
  <nav class="abs nav"><span>HOME</span><span>OUR TEAM</span><span>SERVICES</span><span>PRODUCT</span><span>CONTACT US</span></nav>
</header>

<!-- hero -->
<div class="abs hero-photo" role="img" aria-label="Photo of a business team meeting in a bright office with a presenter standing at the table"></div>
<div class="abs welcome-band"></div>

<section class="abs welcome-card">
  <div class="abs welcome-kicker">WELCOME TO</div>
  <h1 class="abs welcome-title">TALMERO CHARTS</h1>
  <p class="abs welcome-text">Lorem Ipsum is simply dummy text of the printing and typesetting industry. Lorem Ipsum has been the industry's standard dummy text ever since the 1500s, when an unknown printer took a galley of type and scrambled it to make a type specimen book. It has survived not only five centuries, but also the leap into electronic typesetting, remaining essentially unchanged...</p>

  <div class="abs feature" style="left:44px;top:206px">
    <svg class="icon" viewBox="0 0 50 50"><circle cx="25" cy="25" r="23" fill="none" stroke="#6b449b" stroke-width="2"/><rect x="17" y="17" width="16" height="16" fill="none" stroke="#6b449b" stroke-width="2"/><path d="M21 13v4M25 13v4M29 13v4M21 33v4M25 33v4M29 33v4M13 21h4M13 25h4M13 29h4M33 21h4M33 25h4M33 29h4" stroke="#6b449b" stroke-width="1.6"/></svg>
    <h3>Lorem Ipsum is simply...</h3>
    <p>Lorem Ipsum is simply dummy text of the printing and typesetting industry. Lorem Ipsum has been the industry's standard...</p>
  </div>
  <div class="abs feature" style="left:44px;top:373px">
    <svg class="icon" viewBox="0 0 50 50"><circle cx="25" cy="25" r="23" fill="none" stroke="#6b449b" stroke-width="2"/><rect x="14" y="17" width="22" height="16" fill="none" stroke="#6b449b" stroke-width="2"/><path d="M14 17 25 26 36 17" stroke="#6b449b" stroke-width="2" fill="none"/></svg>
    <h3>Lorem Ipsum is simply...</h3>
    <p>Lorem Ipsum is simply dummy text of the printing and typesetting industry. Lorem Ipsum has been the industry's standard...</p>
  </div>
  <div class="abs feature" style="left:582px;top:206px">
    <svg class="icon" viewBox="0 0 50 50"><circle cx="25" cy="25" r="23" fill="none" stroke="#6b449b" stroke-width="2"/><ellipse cx="23" cy="16" rx="8" ry="3" fill="none" stroke="#6b449b" stroke-width="2"/><path d="M15 16v16c0 2 4 3 8 3s8-1 8-3V16M15 24c0 2 4 3 8 3s8-1 8-3" fill="none" stroke="#6b449b" stroke-width="2"/><circle cx="33" cy="33" r="5" fill="#6b449b"/></svg>
    <h3>Lorem Ipsum is simply...</h3>
    <p>Lorem Ipsum is simply dummy text of the printing and typesetting industry. Lorem Ipsum has been the industry's standard...</p>
  </div>
  <div class="abs feature" style="left:582px;top:373px">
    <svg class="icon" viewBox="0 0 50 50"><circle cx="25" cy="25" r="23" fill="none" stroke="#6b449b" stroke-width="2"/><circle cx="25" cy="25" r="4" fill="#6b449b"/><circle cx="16" cy="16" r="3" fill="#6b449b"/><circle cx="34" cy="16" r="3" fill="#6b449b"/><circle cx="16" cy="34" r="3" fill="#6b449b"/><circle cx="34" cy="34" r="3" fill="#6b449b"/><path d="M16 16 34 34M34 16 16 34" stroke="#6b449b" stroke-width="1.6"/></svg>
    <h3>Lorem Ipsum is simply...</h3>
    <p>Lorem Ipsum is simply dummy text of the printing and typesetting industry. Lorem Ipsum has been the industry's standard...</p>
  </div>
</section>

<svg class="abs hexagon" width="202" height="212" viewBox="0 0 202 212" aria-label="Security padlock emblem">
  <polygon points="101,0 199,53 199,159 101,212 3,159 3,53" fill="#fff"/>
  <polygon points="101,8 192,57 192,155 101,204 10,155 10,57" fill="#6b449b"/>
  <polygon points="101,18 184,62 184,150 101,194 18,150 18,62" fill="none" stroke="#9b7bc4" stroke-width="1.5"/>
  <path d="M88 100v-12a13 13 0 0 1 26 0v12" fill="none" stroke="#fff" stroke-width="6"/>
  <rect x="80" y="100" width="42" height="34" rx="3" fill="#fff"/>
  <circle cx="101" cy="114" r="4" fill="#6b449b"/><rect x="99" y="116" width="4" height="9" fill="#6b449b"/>
</svg>

<!-- about -->
<div class="abs about-photo" role="img" aria-label="Portrait photo of the company founder in a dark blazer"></div>
<section class="abs about-box">
  <h2>SHORTLY ABOUT US</h2>
  <p>Lorem Ipsum is simply dummy text of the printing and typesetting industry. Lorem Ipsum has been the industry's standard dummy text ever since the 1500s, when an unknown printer took a galley of type and scrambled it to make a type specimen book. It has survived not only five centuries, but also the leap into electronic typesetting, remaining essentially unchanged. It was popularised in the 1960s with the release of Letraset sheets containing Lorem Ipsum passages, and more recently with desktop publishing software like Aldus PageMaker including versions of Lorem Ipsum.</p>
  <p>Lorem Ipsum is simply dummy text of the printing and typesetting industry. Lorem Ipsum has been type and scrambled it to make a type specimen book. It has survived not only five centuries, but also the leap into electronic typesetting, remaining essentially unchanged. It was popularised in the with desktop publishing software like Aldus PageMaker including versions of Lorem Ipsum.</p>
  <div class="abs about-social"><span class="ring"></span><span class="ring"></span><span class="ring"></span></div>
  <div class="abs read-more">Read More ›</div>
</section>
<div class="abs pager" style="left:582px;top:1578px">
  <span><svg width="10" height="12" viewBox="0 0 10 12"><path d="M7 1 2 6l5 5" stroke="#fff" stroke-width="2" fill="none"/></svg></span>
  <span><svg width="10" height="12" viewBox="0 0 10 12"><path d="M3 1l5 5-5 5" stroke="#fff" stroke-width="2" fill="none"/></svg></span>
</div>

<!-- products -->
<section class="abs products">
  <h2 class="abs section-title"><b>OUR</b> PRODUCTS</h2>
  <div class="abs ribbon">WE OFFER FOR DOWNLOAD</div>
  <div class="abs round-arrow" style="left:95px;top:256px"><svg width="10" height="12" viewBox="0 0 10 12"><path d="M7 1 2 6l5 5" stroke="#fff" stroke-width="2" fill="none"/></svg></div>
  <div class="abs round-arrow" style="left:1064px;top:256px"><svg width="10" height="12" viewBox="0 0 10 12"><path d="M3 1l5 5-5 5" stroke="#fff" stroke-width="2" fill="none"/></svg></div>

  <article class="abs product" style="left:161px;top:148px">
    <div class="shot" role="img" aria-label="Photo of a laptop showing a threat warning on a desk" style="background:linear-gradient(135deg,#8a5a45,#c23a3a 50%,#d8d0c8)"></div>
    <div class="panel"><h3>ADVANCED THREAT PROTECTION</h3><p>Lorem Ipsum is simply dummy text printing and typesetting industry. Lorem Ipsum has been the industry's standard...</p><span class="shop">SHOP NOW</span></div>
  </article>
  <article class="abs product" style="left:463px;top:148px">
    <div class="shot" role="img" aria-label="Photo of a keyboard with an orange security key" style="background:linear-gradient(135deg,#b9d8df,#e0701f 55%,#c3d6da)"></div>
    <div class="panel"><h3>INFORMATION PROTECTION</h3><p>Lorem Ipsum is simply dummy text printing and typesetting industry. Lorem Ipsum has been the industry's standard...</p><span class="shop">SHOP NOW</span></div>
  </article>
  <article class="abs product" style="left:760px;top:148px">
    <div class="shot" role="img" aria-label="Photo of an envelope with a security shield on a blue digital background" style="background:linear-gradient(135deg,#0f3f6d,#3f8fd0 55%,#12355a)"></div>
    <div class="panel"><h3>EMAIL SECURITY</h3><p>Lorem Ipsum is simply dummy text printing and typesetting industry. Lorem Ipsum has been the industry's standard...</p><span class="shop">SHOP NOW</span></div>
  </article>
</section>

<!-- team -->
<svg class="abs team-banner" width="400" height="49" viewBox="0 0 400 49"><polygon points="0,0 400,0 385,24.5 400,49 0,49 15,24.5" fill="#2b2b2b"/><circle cx="30" cy="24.5" r="4" fill="#fff"/><circle cx="370" cy="24.5" r="4" fill="#fff"/></svg>
<div class="abs team-banner"><div class="abs label">OUR TEAM</div></div>

<div class="abs outline-arrow" style="left:224px;top:2442px"><svg width="10" height="12" viewBox="0 0 10 12"><path d="M7 1 2 6l5 5" stroke="#6b449b" stroke-width="2" fill="none"/></svg></div>
<div class="abs outline-arrow" style="left:922px;top:2442px"><svg width="10" height="12" viewBox="0 0 10 12"><path d="M3 1l5 5-5 5" stroke="#6b449b" stroke-width="2" fill="none"/></svg></div>

<div class="abs member" style="left:288px;top:2376px;width:103px;height:161px" role="img" aria-label="Team member portrait photo"></div>
<div class="abs member" style="left:394px;top:2355px;width:105px;height:205px" role="img" aria-label="Team member portrait photo"></div>
<div class="abs member" style="left:681px;top:2355px;width:104px;height:205px" role="img" aria-label="Team member portrait photo"></div>
<div class="abs member" style="left:787px;top:2376px;width:104px;height:161px" role="img" aria-label="Team member portrait photo"></div>
<div class="abs member lead" style="left:501px;top:2334px;width:178px;height:248px" role="img" aria-label="Portrait photo of the senior manager"></div>
<div class="abs name-tag"><strong>DELLAN VOSS</strong><small>Sr. Manager</small></div>

<p class="abs team-text">Lorem Ipsum is simply dummy text of the printing and typesetting industry. Lorem Ipsum has been the industry's standard dummy text ever since the 1500s, when an unknown printer took a galley of type and scrambled it to make a type specimen book...</p>
<div class="abs team-social"><span></span><span></span><span></span><span></span></div>

<!-- payments -->
<div class="abs payments">
  <div class="abs pay" style="left:331px">PayNest</div>
  <div class="abs pay" style="left:447px">Vantra</div>
  <div class="abs pay" style="left:564px">Meridcard</div>
  <div class="abs pay" style="left:682px">Amberline</div>
  <div class="abs pay" style="left:798px">Dovecard</div>
</div>

<!-- footer -->
<footer class="abs footer">
  <div class="abs info-box" style="left:161px">
    <span class="ico"><svg width="14" height="18" viewBox="0 0 14 18"><path d="M7 17S1 10 1 7a6 6 0 0 1 12 0c0 3-6 10-6 10z" fill="none" stroke="#fff" stroke-width="1.6"/><circle cx="7" cy="7" r="2" fill="#fff"/></svg></span>
    <span>Lorem Ipsum is simply dummy text<br>printing and typesetting industry.</span>
  </div>
  <div class="abs info-box" style="left:468px">
    <span class="ico"><svg width="16" height="16" viewBox="0 0 16 16"><path d="M3 1l3 3-2 2c1 2 4 5 6 6l2-2 3 3-2 2C7 15 1 9 1 3z" fill="none" stroke="#fff" stroke-width="1.4"/></svg></span>
    <span>Phone: 0000-000-000<br>Online Booking: 000-000-0000</span>
  </div>
  <div class="abs info-box" style="left:766px">
    <span class="ico"><svg width="18" height="13" viewBox="0 0 18 13"><rect x="1" y="1" width="16" height="11" fill="none" stroke="#fff" stroke-width="1.4"/><path d="M1 1l8 6 8-6" fill="none" stroke="#fff" stroke-width="1.4"/></svg></span>
    <span>info@talmerocharts.example</span>
  </div>

  <div class="abs foot-col" style="left:161px">
    <h4>ABOUT US</h4>
    <p>Lorem Ipsum is simply dummy text of the printing and typesetting industry. Lorem Ipsum has been the industry unknown printer took a galley of type and scrambled it to make a type specimen book.</p>
    <p class="more">Read More »</p>
    <div class="foot-social"><span></span><span></span><span></span><span></span></div>
  </div>
  <div class="abs foot-col" style="left:565px">
    <h4>INFORMATION</h4>
    <ul class="foot-list"><li>Home</li><li>Our Team</li><li>Services</li><li>Product</li><li>Contact us</li></ul>
  </div>
  <div class="abs foot-col" style="left:836px">
    <h4>NEWSLETTER</h4>
    <div class="email-field">Enter Your Email Id</div>
    <div class="subscribe">SUBSCRIBE</div>
  </div>
</footer>
<div class="abs copyright">Copyright 2018. All Right Reserved.</div>

</body>
</html>
```